Upbeat Accouting Package Flyer

I am looking for a 1 page (front, or front and back) flyer that will become our marketing for our accounting services. We are looking for something a little different and we are catering to the small retail shop owners. We have 3 accounting packages we would like to display and then some add-ons. I have included our logo that must be included in the design. I have uploaded the accounting package information as well.
Target Market(s)
Small Retail Shop Owners
Industry/Entity Type
Accounting
Colors
Designer to choose colors to be used in the design.
Requirements
Must have
- A casual feel. We are not your typical accountants who are very professional and "stuffy". I want it to feel like we are all family.
Nice to have
- I would like to incorporate some sort of retail theme.
- We have a couple of taglines we like to use and it would be great if they could be included. They are "We know you CAN do the accounting, but do you WANT to?" and "We allow you to get back to what's important."
Should not have
- Typical stock accounting photos of people shaking hands, large office buildings, etc.

```html
<!DOCTYPE html>
<html lang="en">
<head>
<meta charset="utf-8">
<title>Accounting Packages Flyer</title>
<link rel="stylesheet" href="https://fonts.googleapis.com/css2?family=Oswald:wght@500;600&family=Roboto:wght@400;500;700&family=Roboto+Condensed:wght@700&display=swap">
<style>
:root{
  --cyan:#1fbcd8;
  --cyan-light:#a8e1ee;
  --ink:#0b0b0b;
  --grey-row:#7d7d7d;
  --grey-text:#3a3a3a;
  --white:#ffffff;
  --page:#ffffff;
}
*{box-sizing:border-box;margin:0;padding:0}
html,body{width:946px;height:1200px;overflow:hidden;background:var(--page)}
body{font-family:'Roboto',Arial,sans-serif;color:var(--ink)}
.flyer{position:relative;width:946px;height:1200px;background:var(--page);overflow:hidden}
.hero-photo{position:absolute;left:0;top:0;width:946px;height:493px;
  background:linear-gradient(180deg,#6b4a2a 0%,#b98b57 35%,#8a6440 65%,#4a3526 100%)}
.brand-box{position:absolute;left:558px;top:52px;width:388px;height:99px;background:var(--white);
  display:flex;align-items:center;justify-content:center;gap:12px}
.brand-dot{width:14px;height:14px;border-radius:50%;background:var(--cyan)}
.brand-name{font-family:'Roboto',sans-serif;font-weight:500;font-size:26px;color:#1d1d1d;line-height:1.1}
.title-band{position:absolute;left:201px;top:246px;width:514px;height:75px;background:rgba(70,62,56,.72);
  display:flex;align-items:center;justify-content:center}
.title-band h1{font-family:'Oswald',sans-serif;font-weight:500;font-size:50px;color:var(--white);letter-spacing:.5px}
.cyan-strip{position:absolute;left:0;top:493px;width:946px;height:14px;background:var(--cyan)}
.package{position:absolute;display:flex;flex-direction:column}
.package.side{top:427px;width:248px;height:527px;background:var(--cyan)}
.package.develop{left:62px}
.package.relax{left:636px}
.package.grow{left:332px;top:353px;width:283px;height:644px;background:var(--ink);box-shadow:0 4px 10px rgba(0,0,0,.35)}
.pill{font-family:'Roboto Condensed',sans-serif;font-weight:700;font-size:31px;text-align:center;border-radius:12px;line-height:40px}
.side .pill{margin:6px 14px 0;background:var(--ink);color:var(--white)}
.grow .pill{margin:11px 14px 0;background:var(--white);color:var(--ink)}
.icon-area{display:flex;flex-direction:column;align-items:center;justify-content:center}
.develop .icon-area{height:49px}
.relax .icon-area{height:52px}
.grow .icon-area{height:90px}
.tagline{font-size:14px;color:var(--white);margin-top:2px}
.figure-slot{width:60px;height:42px;background:#0d0d0d;border-radius:4px}
.row{display:flex;align-items:center;padding:0 8px 0 12px;font-size:15.5px;line-height:16px;flex:0 0 auto}
.row::before{content:"\2713";font-size:14px;margin-right:6px;align-self:flex-start;margin-top:1px}
.row.plain::before{content:"";margin-right:20px}
.side .row{color:var(--ink)}
.side .row.alt{background:var(--cyan-light)}
.grow .row{color:var(--white);padding-left:14px;line-height:21px}
.grow .row.alt{background:var(--grey-row)}
.relax .row{font-size:15px;padding-left:8px}
.fill{flex:1 1 auto}
.options{position:absolute;left:62px;top:1006px}
.options h2,.contact h2{font-family:'Roboto Condensed',sans-serif;font-weight:700;font-size:19px;color:var(--ink);margin-bottom:6px}
.options li{list-style:none;font-size:15.5px;color:var(--grey-text);line-height:19px;margin-bottom:4px;padding-left:20px;position:relative}
.options li::before{content:"\2713";position:absolute;left:0;color:var(--ink)}
.contact{position:absolute;right:55px;top:1006px;text-align:right}
.contact p{font-size:15.5px;color:var(--grey-text);line-height:19px;margin-bottom:5px;display:flex;justify-content:flex-end;align-items:center;gap:10px}
.contact p svg{width:14px;height:14px;flex:0 0 14px;fill:#555}
.contact .addr{line-height:20px}
.bottom-band{position:absolute;left:0;top:1186px;width:946px;height:14px;background:var(--cyan)}
</style>
</head>
<body>
<main class="flyer">
  <div class="hero-photo" role="img" aria-label="Photo of a bright boutique retail store interior with clothing racks and display counters"></div>

  <div class="brand-box">
    <span class="brand-dot"></span>
    <span class="brand-name">Ledgerline<br>Tax and Accounting Inc.</span>
  </div>

  <div class="title-band"><h1>ACCOUNTING PACKAGES</h1></div>
  <div class="cyan-strip"></div>

  <section class="package side develop">
    <div class="pill">DEVELOP</div>
    <div class="icon-area">
      <svg width="80" height="60" viewBox="0 0 80 60" fill="none" stroke="#0b0b0b" stroke-width="2.2" aria-hidden="true">
        <circle cx="40" cy="26" r="13"/>
        <path d="M34 39h12v8H34z"/>
        <path d="M36 51h8"/>
        <path d="M40 6V1M24 12l-4-4M56 12l4-4M62 20l12-10m0 0h-6m6 0v6M18 30l-8 4"/>
      </svg>
    </div>
    <div class="row alt" style="height:57px">$300/mo when paid annually $325/mo billed monthly</div>
    <div class="row" style="height:41px">CloudBooks Online subscription</div>
    <div class="row alt" style="height:42px">Free accounting setup</div>
    <div class="row" style="height:38px">Weekly transaction processing</div>
    <div class="row alt" style="height:41px">Monthly account reconciliation (up to 2 accounts)</div>
    <div class="row" style="height:68px;align-items:flex-start;padding-top:8px;line-height:20px">Monthly financial statements by the 15th of the month</div>
    <div class="fill"></div>
  </section>

  <section class="package grow">
    <div class="pill">GROW</div>
    <div class="icon-area">
      <svg width="80" height="66" viewBox="0 0 80 66" fill="#ffffff" aria-hidden="true">
        <rect x="6" y="44" width="11" height="22"/>
        <rect x="22" y="34" width="11" height="32"/>
        <rect x="38" y="40" width="11" height="26"/>
        <path d="M2 46 L26 20 L42 32 L66 8 L60 4 L78 0 L74 18 L70 12 L42 40 L26 28 L6 50Z"/>
      </svg>
    </div>
    <div class="row alt" style="height:52px;line-height:19px">$550/mo billed annually;<br>$575/mo billed monthly</div>
    <div class="row" style="height:34px">CloudBooks Online subscription</div>
    <div class="row alt" style="height:44px">Free accounting setup</div>
    <div class="row" style="height:37px">Weekly transaction processing</div>
    <div class="row alt" style="height:52px;line-height:19px">Monthly account reconciliation (up to 4 accounts)</div>
    <div class="row" style="height:50px;line-height:22px">Monthly financial statements by the 10th of the month</div>
    <div class="row alt" style="height:52px;line-height:22px">Client portal access for document sharing</div>
    <div class="row" style="height:42px">1 Custom Report</div>
    <div class="row alt" style="height:44px">Accounts Payable</div>
    <div class="row plain" style="height:96px;line-height:22px;padding-left:0">Monthly Scorecard (customized metric tracking for your business)</div>
    <div class="fill"></div>
  </section>

  <section class="package side relax">
    <div class="pill">RELAX</div>
    <div class="icon-area">
      <div class="figure-slot" role="img" aria-label="Small icon of a person relaxing in a reclined chair"></div>
      <div class="tagline">(We've Got This)</div>
    </div>
    <div class="row alt" style="height:42px">$850/mo billed annually;<br>$875/mo billed monthly</div>
    <div class="row" style="height:24px">CloudBooks Online subscription</div>
    <div class="row alt" style="height:29px">Free accounting setup</div>
    <div class="row" style="height:24px">Weekly transaction processing</div>
    <div class="row alt" style="height:42px">Monthly account reconciliation (up to 5-10 accounts)</div>
    <div class="row" style="height:45px">Monthly financial statements by the 5th of the month</div>
    <div class="row alt" style="height:43px">Client portal access for document sharing</div>
    <div class="row" style="height:23px">2 Custom Reports</div>
    <div class="row alt" style="height:24px">Accounts Payable</div>
    <div class="row" style="height:39px">Invoicing and accounts receivable</div>
    <div class="row alt" style="height:56px">Weekly Scorecard (customized metric tracking for your business)</div>
    <div class="fill"></div>
  </section>

  <section class="options">
    <h2>ADDITIONAL OPTIONS</h2>
    <ul>
      <li>Payroll – 1-10 employees $85/mo;<br>11-30 employees $175/mo</li>
      <li>Sales tax - $30/mo per state</li>
      <li>Corporate taxes $50/mo</li>
      <li>Owner taxes - $25/mo</li>
    </ul>
  </section>

  <section class="contact">
    <h2>LEDGERLINE TAX AND ACCOUNTING INC.</h2>
    <p class="addr"><span>4820 W. 71st Street<br>Merriam, KS 66203</span>
      <svg viewBox="0 0 14 14" aria-hidden="true"><path d="M7 0a5 5 0 0 1 5 5c0 4-5 9-5 9S2 9 2 5a5 5 0 0 1 5-5zm0 3a2 2 0 1 0 0 4 2 2 0 0 0 0-4z"/></svg></p>
    <p>(913) 555-0142
      <svg viewBox="0 0 14 14" aria-hidden="true"><path d="M3 0l3 3-2 2c1 2 3 4 5 5l2-2 3 3-2 3C6 14 0 8 0 2z"/></svg></p>
    <p>hello@ledgerline-kc.com
      <svg viewBox="0 0 14 14" aria-hidden="true"><path d="M0 3h14v9H0zM1 4l6 4 6-4"/></svg></p>
    <p>www.ledgerlinekc.com
      <svg viewBox="0 0 14 14" aria-hidden="true"><path d="M7 0a7 7 0 1 0 0 14A7 7 0 0 0 7 0zm0 1.4a5.6 5.6 0 1 1 0 11.2A5.6 5.6 0 0 1 7 1.4zM1.4 6.4h11.2v1.2H1.4zM6.4 1.4h1.2v11.2H6.4z"/></svg></p>
  </section>

  <div class="bottom-band"></div>
</main>
</body>
</html>
```